Visitenkarten-Design für  Softwareunternehmen
Visitenkarten-Design für Softwareunternehmen
Toller Designer! Ist immer auf Vorschläge eingegangen und hat diese umgesetzt. Bin sehr zufrieden mit dem Ergebnis.
Zielgruppe
Wir sind ein B2B Softwareunternehmen, das eine Energiemonitoringsoftware für die mittelständische Industrie entwickelt hat. Das heißt unsere Visitenkarten werden überwiegend an unsere Zielgruppe, d.h. Geschäftsführer produzierender mittelständischer Industrie ausgehändigt.
Aufgabenstellung
Gleichzeitig treten wir nach außen jung, innovativ und voller Tatendrang auf. Ganz nach unserer Vision: Voll Energie. Null Emission. (Auch gerne auf der Visitenkarte mit aufnehmen). Uns ist es wichtig, unser CI nach außen zu kommunizieren und unsere Webseite auf der Visitenkarte zu platzieren.
Die Visitenkarte soll einzeln für jeden MitarbeiterIn personalisiert werden können.

```html
<!DOCTYPE html>
<html lang="de">
<head>
<meta charset="utf-8">
<title>Voltara Visitenkarte</title>
<link rel="stylesheet" href="https://fonts.googleapis.com/css2?family=Open+Sans:wght@400;600;700;800&display=swap">
<style>
  :root {
    --page-bg: #d9dcde;
    --card-dark: #2c3a40;
    --card-light: #ffffff;
    --ink-dark: #2c3a40;
    --ink-soft: #3e4a50;
    --ink-white: #ffffff;
    --rule-grey: #8a9094;
  }
  * { margin: 0; padding: 0; box-sizing: border-box; }
  html, body {
    width: 1200px; height: 900px; overflow: hidden;
    background: var(--page-bg);
    font-family: "Open Sans", Arial, sans-serif;
  }
  .sheet {
    width: 1200px; height: 900px;
    display: flex; flex-direction: column;
    align-items: center; justify-content: center; gap: 44px;
  }
  .card {
    width: 620px; height: 376px; position: relative;
    box-shadow: 0 6px 18px rgba(0,0,0,.18);
  }
  /* front */
  .card--front { background: var(--card-dark); color: var(--ink-white); }
  .card--front .brand-name {
    position: absolute; left: 0; right: 0; top: 128px;
    text-align: center; font-weight: 800; font-size: 68px; letter-spacing: 2px;
  }
  .card--front .web-band {
    position: absolute; left: 0; right: 0; bottom: 46px;
    display: flex; align-items: center; gap: 14px;
  }
  .web-band .rule { height: 2px; background: var(--ink-white); }
  .web-band .rule--left { width: 212px; }
  .web-band .rule--right { flex: 1; }
  .web-band .url { font-size: 15px; letter-spacing: .3px; }
  /* back */
  .card--back { background: var(--card-light); color: var(--ink-dark); }
  .card--back .brand-name {
    position: absolute; left: 46px; top: 92px; width: 220px;
    font-weight: 800; font-size: 40px; letter-spacing: 1px; text-align: center;
  }
  .card--back .divider {
    position: absolute; left: 302px; top: 60px; width: 1.5px; height: 256px;
    background: var(--rule-grey);
  }
  .contact {
    position: absolute; left: 332px; top: 64px; color: var(--ink-soft);
  }
  .contact .person { font-weight: 700; font-size: 19px; color: var(--ink-dark); line-height: 1.2; }
  .contact .role { font-size: 15px; margin-bottom: 16px; }
  .contact .address { font-size: 15px; line-height: 1.35; margin-bottom: 10px; }
  .contact ul { list-style: none; }
  .contact li {
    display: flex; align-items: center; gap: 10px;
    font-size: 19px; line-height: 1.35; color: var(--ink-dark);
  }
  .contact svg { width: 16px; height: 16px; flex: none; }
</style>
</head>
<body>
<main class="sheet">
  <section class="card card--front" aria-label="Vorderseite">
    <div class="brand-name">Voltara</div>
    <div class="web-band">
      <span class="rule rule--left"></span>
      <span class="url">www.voltara.example</span>
      <span class="rule rule--right"></span>
    </div>
  </section>

  <section class="card card--back" aria-label="Rückseite">
    <div class="brand-name">Voltara</div>
    <div class="divider"></div>
    <div class="contact">
      <div class="person">Vorname Name</div>
      <div class="role">Position</div>
      <div class="address">Lindenweg 8<br>88410 Seestadt</div>
      <ul>
        <li>
          <svg viewBox="0 0 16 16" aria-hidden="true"><path d="M3 1.5l3 .5 1 3-1.8 1.3a9 9 0 0 0 4.5 4.5L11 9l3 1 .5 3-2 2C6 14.5 1.5 10 1 3.5z" fill="currentColor"/></svg>
          +49 000 1234 5678
        </li>
        <li>
          <svg viewBox="0 0 16 16" aria-hidden="true"><rect x="4" y="1" width="8" height="14" rx="1.5" fill="none" stroke="currentColor" stroke-width="1.4"/><circle cx="8" cy="12.5" r=".9" fill="currentColor"/></svg>
          +49 000 8765 4321
        </li>
        <li>
          <svg viewBox="0 0 16 16" aria-hidden="true"><rect x="1" y="3" width="14" height="10" fill="currentColor"/><path d="M1.5 3.5L8 9l6.5-5.5" fill="none" stroke="#fff" stroke-width="1.2"/></svg>
          info@voltara.example
        </li>
        <li>
          <svg viewBox="0 0 16 16" aria-hidden="true"><circle cx="8" cy="8" r="6.5" fill="none" stroke="currentColor" stroke-width="1.4"/><ellipse cx="8" cy="8" rx="2.8" ry="6.5" fill="none" stroke="currentColor" stroke-width="1.1"/><path d="M1.5 8h13M2.5 5h11M2.5 11h11" stroke="currentColor" stroke-width="1"/></svg>
          www.voltara.example
        </li>
      </ul>
    </div>
  </section>
</main>
</body>
</html>
```